Anzeigengestaltung für einen einen ambulanten Pflegedienst
Zielgruppe
Insgesamt möchte ich gern drei Anzeigen für das Internet gestalten haben. Ich betreibe einen ambulanten Pflegedienst. Die erste Anzeige soll dazu dienen Kunden anzusprechen, die einen Unterstützungsbedarf und / oder einen Beratungsbedarf haben. Die zweite Anzeige soll dazu dienen neues Personal anzuwerben. Die dritte Anzeige soll speziell potenzielle Azubis ansprechen. Die Anzeigen sind gedacht für Chatterwall und Pixelora hauptsächlich. In den Druck sollte es schon 10cm x 8cm sein. Es wäre super wenn vielleicht auch eine Art Aufruf an ehrenamtliche Mitarbeiter erfolgt.
Aufgabenstellung
Die Anzeigen sollen den Stil der Homepage beibehalten. Freundlich, frisch und agil wirken. Alle sollten emotional ansprechend sein und gerade der für zukünftige Mitarbeiter sollte deutlich ein gutes Betriebsklima vermitteln. Als Datei habe ich einige Bilder, die bereits für die Homepage oder Flyer verwendet wurden hochgeladen. des Weiteren habe ich die einzelnen Seiten des Flyers hochgeladen.

```html
<!DOCTYPE html>
<html lang="de">
<head>
<meta charset="utf-8">
<title>Ausbildung Pflege – Helvo Pflege</title>
<link rel="stylesheet" href="https://fonts.googleapis.com/css2?family=Playfair+Display:wght@400&family=Quicksand:wght@500;700&display=swap">
<style>
  :root {
    --teal: #4ab0ac;
    --green: #7ab03a;
    --text: #666666;
    --band: #e1f0f8;
    --white: #ffffff;
    --ring: #eef0ec;
  }
  html, body { margin: 0; padding: 0; overflow: hidden; }
  body { width: 1200px; height: 960px; background: var(--white); }
  .ad {
    position: relative; width: 1200px; height: 960px; overflow: hidden;
    background: var(--white); font-family: "Quicksand", sans-serif; color: var(--text);
  }
  .hero-visual { position: absolute; left: 0; top: 0; width: 1200px; height: 960px; }
  .kicker {
    position: absolute; left: 60px; top: 60px; margin: 0;
    font-family: "Playfair Display", serif; font-weight: 400; font-size: 37px; color: var(--text);
  }
  .headline {
    position: absolute; left: 58px; top: 118px; margin: 0;
    font-weight: 700; font-size: 64px; line-height: 76px; color: var(--teal);
  }
  .headline .accent { color: var(--green); }
  .rule { position: absolute; left: 60px; top: 294px; width: 303px; height: 6px; background: var(--green); }
  .intro {
    position: absolute; left: 60px; top: 350px; margin: 0;
    font-weight: 500; font-size: 31px; line-height: 42.5px; letter-spacing: 0.5px;
  }
  .requirements {
    position: absolute; top: 570px; margin: 0; padding: 0; list-style: none;
    font-weight: 500; font-size: 33px; line-height: 47px; letter-spacing: 0.5px;
  }
  .requirements li { position: relative; padding-left: 29px; margin-bottom: 12px; }
  .requirements li::before { content: "+"; position: absolute; left: 0; color: var(--green); }
  .requirements.left { left: 60px; }
  .requirements.right { left: 622px; }
  .footer-band { position: absolute; left: 0; top: 810px; width: 1200px; height: 150px; background: var(--band); }
  .pill {
    position: absolute; top: 854px; height: 62px; border-radius: 31px; color: var(--white);
    font-family: "Playfair Display", serif; font-size: 35px; line-height: 62px; text-align: center;
  }
  .pill.greeting { left: 35px; width: 295px; background: var(--green); }
  .pill.url { left: 354px; width: 586px; background: var(--teal); }
  .brand-badge {
    position: absolute; left: 957px; top: 700px; width: 210px; height: 210px; border-radius: 50%;
    background: var(--white); border: 4px solid var(--ring); box-sizing: border-box;
    display: flex; flex-direction: column; align-items: center; justify-content: center; gap: 14px;
  }
  .brand-badge .dot { width: 44px; height: 44px; border-radius: 50%; background: var(--teal); }
  .brand-badge .name { font-weight: 700; font-size: 22px; color: var(--text); letter-spacing: 0.3px; }
</style>
</head>
<body>
<main class="ad">
  <svg class="hero-visual" viewBox="0 0 1200 960" aria-hidden="false">
    <defs>
      <clipPath id="photo-round"><circle cx="1030" cy="60" r="483"/></clipPath>
      <linearGradient id="photo-tones" x1="0" y1="0" x2="1" y2="0.6">
        <stop offset="0" stop-color="#1f9c94"/>
        <stop offset="0.45" stop-color="#2b8f88"/>
        <stop offset="0.62" stop-color="#c99a86"/>
        <stop offset="1" stop-color="#e4dde8"/>
      </linearGradient>
    </defs>
    <rect x="540" y="0" width="660" height="560" fill="url(#photo-tones)" clip-path="url(#photo-round)"
          role="img" aria-label="Foto: Pflegekraft in grüner Dienstkleidung hört eine Patientin mit dem Stethoskop ab"/>
    <path class="arc-teal" d="M556 353 C556 300 585 275 640 270 C670 267 700 270 712 278" fill="none" stroke="#4ab0ac" stroke-width="6" stroke-linecap="round"/>
    <path class="arc-green" d="M583 413 C585 360 595 330 610 315 C640 295 700 300 732 320" fill="none" stroke="#7ab03a" stroke-width="6" stroke-linecap="round"/>
  </svg>

  <p class="kicker">Komm in unser Team Pflege</p>
  <h1 class="headline">Wir bilden<br><span class="accent">DICH</span> aus!</h1>
  <div class="rule"></div>

  <p class="intro">Hilf uns die Pflege in der<br>Umgebung Dessau-Roßlau<br>qualitativ zu verbessern und<br>menschlicher zu gestalten.</p>

  <ul class="requirements left">
    <li>Teamfähigkeit</li>
    <li>Hilfsbereitschaft</li>
    <li>Engagement</li>
  </ul>
  <ul class="requirements right">
    <li>Führerschein Klasse B</li>
    <li>Gute Deutschkenntnisse<br>in Wort/Schrift</li>
  </ul>

  <div class="footer-band"></div>
  <div class="pill greeting">Wir freuen uns!</div>
  <div class="pill url">www.helvo-pflege.de/karriere/</div>

  <div class="brand-badge">
    <span class="dot"></span>
    <span class="name">HELVO PFLEGE</span>
  </div>
</main>
</body>
</html>
```